A start-up named "Corvath Therapeutics" - needs a new PowerPoint design

We need a new PowerPoint Design for an early-stage start-up named "Corvath Therapeutics" seeking to disrupt the current approach towards drug discovery within aging disorders.

We would like to build on Corvath's legacy, the founder of the modern science of genetics, by employing a multidisciplinary approach, experimenting, and providing elderly patients the attention they deserve.

We have selected the suffix "therapeutics" intentionally as it stands for (a medicine) the treatment of disease; the science of healing. Alzheimer’s treatment is a huge, urgent, unmet need:
- Shift from a disease-management system to a preventive medicine system
- Focus on increasing the health span, not only the life span

Target Market(s)

Pharma/ Biotech Executives Medical Institutions Healthcare professionals (MDs, nurses, payors, pharmacists, etc.) Patients

Industry/Entity Type

Healthcare

Other font styles liked:
• Celias

Colors
0054AA
0677BA
7BADD7
CADEEF
E8F1F8
E54698
E96AAD
F1A4CE
F9D9EA
FCEFF6
A7469A
B969AE
D3A5CF
EDDBEB
F8F0F9
6B429C
8869AF
B7A5CE
E3DAEB
F3F0F8

Requirements
Must have
• - differentiate from other companies named after Corvath - differentiate from other Pharma/ Biotech companies
Nice to have
• simplicity/ minimalist logo vivid colors gradient 3D Life-Sciences inspired Simple geometry Balance
Should not have
• mascot/ emblem watermark logo animated ink style nature-inspired inventive typography artistic chaos

```html
<!DOCTYPE html>
<html lang="en">
<head>
<meta charset="utf-8">
<title>Corvath Therapeutics – Presentation Template</title>
<link rel="stylesheet" href="https://fonts.googleapis.com/css2?family=Lexend:wght@400;500;600;700&family=Montserrat:wght@400;500;600;700&display=swap">
<style>
:root{
  --blue:#0054AA; --blue-2:#0677BA; --blue-light:#7BADD7; --blue-pale:#CADEEF; --blue-mist:#E8F1F8;
  --pink:#E54698; --pink-2:#E96AAD; --pink-light:#F1A4CE;
  --purple:#6B429C; --orchid:#A7469A; --orchid-2:#B969AE; --lilac:#8869AF;
  --ink:#232323; --text:#444; --muted:#9a9a9a; --stage:#dcdcdc; --dark:#262626; --navy:#17305a;
}
*{box-sizing:border-box;margin:0;padding:0}
html,body{width:667px;height:1200px;overflow:hidden}
body{background:var(--stage);position:relative;font-family:Montserrat,sans-serif;color:var(--text)}

.slide{position:absolute;width:437px;height:245px;background:#fff;overflow:hidden;transform-origin:0 0;transform:scale(.4665)}
.slide.hero{transform:scale(.982)}
.abs{position:absolute}
.s-title{position:absolute;left:23px;top:18px;font:500 16px Lexend,sans-serif;color:var(--ink)}
.brand{position:absolute;right:22px;top:22px;display:flex;align-items:center;gap:3px;font:600 7px Montserrat,sans-serif;color:var(--blue)}
.brand .mark{width:7px;height:7px;background:var(--blue)}
.foot{position:absolute;left:0;right:0;bottom:0;height:12px;background:linear-gradient(90deg,var(--purple),var(--orchid) 55%,var(--pink));font:600 3px Montserrat,sans-serif;color:#fff;padding:4.5px 6px}
.foot .num{position:absolute;right:0;top:0;width:36px;height:12px;background:var(--pink);text-align:center;padding-top:4.5px;font-size:4px}
.lorem{font-size:4px;line-height:1.25;color:var(--text)}
.h-blue{color:var(--blue);font-weight:600}
.h-light{color:var(--blue-light);font-weight:600}
.h-pink{color:var(--pink);font-weight:600}
.h-orchid{color:var(--orchid-2);font-weight:600}
ul.bul{list-style:none}
ul.bul li{position:relative;padding-left:6px;margin-bottom:3px}
ul.bul li::before{content:"";position:absolute;left:0;top:1.2px;width:2px;height:2px;background:var(--blue)}
.photo{position:absolute}

/* title slides */
.cover .logo{position:absolute;left:27px;top:36px;display:flex;align-items:center;gap:4px;font:600 9px Montserrat,sans-serif;color:var(--blue)}
.cover .logo .mark{width:9px;height:9px;background:var(--blue)}
.cover .name{position:absolute;left:27px;top:84px;font:600 21px/1.05 Lexend,sans-serif;letter-spacing:-.2px}
.cover .name .a{color:var(--blue);display:block}
.cover .name .b{color:var(--pink);display:block}
.cover .date{position:absolute;left:27px;top:133px;font-size:4.5px;color:var(--ink)}
.cover .copy{position:absolute;left:27px;top:172px;font-size:3.6px;color:#c8c8c8}
.cover.dark .logo,.cover.dark .name .a,.cover.dark .date,.cover.dark .copy,
.cover.blue .logo,.cover.blue .name .a,.cover.blue .name .b,.cover.blue .date,.cover.blue .copy{color:#fff}
.cover.dark .logo .mark,.cover.blue .logo .mark{background:#fff}

/* agenda */
.agenda-item{position:absolute;width:130px;display:flex;gap:10px}
.agenda-item .n{font:400 11px Lexend,sans-serif;color:#cfcfcf;width:10px}
.agenda-item .t{font-size:4.8px;font-weight:600}

/* team */
.member{position:absolute;top:30px;width:100px;text-align:center}
.member .av{width:38px;height:38px;border-radius:50%;margin:0 auto 6px;background:radial-gradient(circle at 50% 40%,#cfcfcf,#8d8d8d)}
.member .nm{font-size:5px;font-weight:600}
.member .jt{font-size:3.6px;margin:2px 0 4px;color:var(--ink)}

/* icon row */
.feat{position:absolute;top:70px;width:85px;text-align:center}
.feat .ic{width:22px;height:22px;border-radius:50%;margin:0 auto 4px;display:flex;align-items:center;justify-content:center}
.feat .hd{font-size:5px;font-weight:600;margin-bottom:3px}

/* columns */
.col3{position:absolute;top:44px;width:120px}
.col3 .hd{font-size:5px;font-weight:600;margin-bottom:6px}

/* timeline */
.tl-dot{position:absolute;top:124px;width:13px;height:13px;border-radius:50%;color:#fff;font:500 7px Lexend,sans-serif;text-align:center;line-height:13px}
.tl-txt{position:absolute;width:60px;text-align:center;font-size:3.4px}
.tl-txt .hd{font-size:4.5px;font-weight:600;line-height:1.1}

/* table */
.tbl{position:absolute;left:23px;top:46px;width:390px;border-collapse:collapse;font-size:3.6px}
.tbl td{height:9.5px;border-bottom:.5px solid #e5e5e5;padding-left:2px}
.tbl .tick{text-align:center}

/* quotes */
.quote{position:absolute;top:46px;width:93px;height:172px;color:#fff;padding:10px 7px;font-size:4.7px;line-height:1.2}
.quote .q{font:700 14px Lexend,sans-serif;line-height:1;margin-bottom:8px}

/* contact */
.contact .logo{position:absolute;left:20px;top:84px;display:flex;align-items:center;gap:4px;font:600 9px Montserrat,sans-serif;color:#fff}
.contact .logo .mark{width:9px;height:9px;background:#fff}
.contact .line{position:absolute;left:20px;font-size:4px;color:#fff;display:flex;align-items:center;gap:4px}
</style>
</head>
<body>

<!-- ===== Featured title slide ===== -->
<section class="slide cover hero" style="left:119px;top:56px">
  <svg class="photo" width="437" height="245" viewBox="0 0 437 245" role="img" aria-label="Photo of a lab researcher in a mask reading a tablet">
    <defs><linearGradient id="ph1" x1="0" y1="0" x2="1" y2="1"><stop offset="0" stop-color="#e6ebf0"/><stop offset=".6" stop-color="#c9d0d9"/><stop offset="1" stop-color="#9aa6b6"/></linearGradient></defs>
    <rect width="437" height="245" fill="url(#ph1)"/>
  </svg>
  <svg class="abs" style="left:0;top:0" width="437" height="245" viewBox="0 0 437 245">
    <polygon points="111,0 170,0 310,123 258,123" fill="#0054AA" opacity=".85"/>
    <polygon points="258,123 310,123 200,245 111,245" fill="#E54698" opacity=".45"/>
    <polygon points="290,0 330,0 330,245 300,245 390,123" fill="#7BADD7" opacity=".18"/>
    <polygon points="0,0 111,0 258,123 111,245 0,245" fill="#fff"/>
  </svg>
  <div class="logo"><span class="mark"></span>Corvath Therapeutics</div>
  <div class="name"><span class="a">Corvath</span><span class="b">Therapeutics</span></div>
  <div class="date">Wednesday, January 12, 2022</div>
  <div class="copy">© 2021 Corvath Therapeutics, All Rights Reserved.</div>
</section>

<!-- ===== Row 1: title variants ===== -->
<section class="slide cover" style="left:18px;top:435px">
  <svg class="photo" width="437" height="245" viewBox="0 0 437 245" role="img" aria-label="Photo of a lab researcher in a mask reading a tablet">
    <rect width="437" height="245" fill="url(#ph1)"/>
    <polygon points="111,0 170,0 310,123 258,123" fill="#0054AA" opacity=".85"/>
    <polygon points="258,123 310,123 200,245 111,245" fill="#E54698" opacity=".45"/>
    <polygon points="0,0 111,0 258,123 111,245 0,245" fill="#fff"/>
  </svg>
  <div class="logo"><span class="mark"></span>Corvath Therapeutics</div>
  <div class="name"><span class="a">Corvath</span><span class="b">Therapeutics</span></div>
  <div class="date">Wednesday, January 12, 2022</div>
  <div class="copy">© 2021 Corvath Therapeutics, All Rights Reserved.</div>
</section>

<section class="slide cover dark" style="left:232px;top:435px">
  <svg class="photo" width="437" height="245" viewBox="0 0 437 245" role="img" aria-label="Photo of a scientist working with lab samples">
    <defs><linearGradient id="ph2" x1="0" y1="0" x2="1" y2="1"><stop offset="0" stop-color="#d9e2ec"/><stop offset=".5" stop-color="#8aa3c2"/><stop offset="1" stop-color="#3d5c8c"/></linearGradient></defs>
    <rect width="437" height="245" fill="url(#ph2)"/>
    <polygon points="111,0 170,0 310,123 258,123" fill="#0054AA" opacity=".85"/>
    <polygon points="258,123 310,123 200,245 111,245" fill="#E54698" opacity=".45"/>
    <polygon points="0,0 111,0 258,123 111,245 0,245" fill="#262626"/>
  </svg>
  <div class="logo"><span class="mark"></span>Corvath Therapeutics</div>
  <div class="name"><span class="a">Corvath</span><span class="b">Therapeutics</span></div>
  <div class="date">Wednesday, January 12, 2022</div>
  <div class="copy">© 2021 Corvath Therapeutics, All Rights Reserved.</div>
</section>

<section class="slide cover blue" style="left:445px;top:435px">
  <svg class="photo" width="437" height="245" viewBox="0 0 437 245" role="img" aria-label="Photo of hands holding a tablet in a clinic">
    <defs><linearGradient id="ph3" x1="0" y1="0" x2="1" y2="1"><stop offset="0" stop-color="#dfe7ef"/><stop offset=".6" stop-color="#b7c5d4"/><stop offset="1" stop-color="#c49a8c"/></linearGradient></defs>
    <rect width="437" height="245" fill="url(#ph3)"/>
    <polygon points="111,0 170,0 310,123 258,123" fill="#0054AA" opacity=".7"/>
    <polygon points="258,123 310,123 200,245 111,245" fill="#E54698" opacity=".45"/>
    <polygon points="0,0 111,0 258,123 111,245 0,245" fill="#0054AA"/>
  </svg>
  <div class="logo"><span class="mark"></span>Corvath Therapeutics</div>
  <div class="name"><span class="a">Corvath</span><span class="b">Therapeutics</span></div>
  <div class="date">Wednesday, January 12, 2022</div>
  <div class="copy">© 2021 Corvath Therapeutics, All Rights Reserved.</div>
</section>

<!-- ===== Row 2 ===== -->
<section class="slide" style="left:18px;top:559px">
  <h2 class="s-title">Agenda Slide</h2>
  <div class="brand"><span class="mark"></span>Corvath</div>
  <div class="agenda-item" style="left:58px;top:74px"><span class="n">1</span><div><div class="t h-blue">Title Goes Here</div><p class="lorem">Lorem ipsum dolor sit amet, consectetur adipiscing elit. Vivamus eu dui ex.</p></div></div>
  <div class="agenda-item" style="left:228px;top:74px"><span class="n">2</span><div><div class="t h-light">Title Goes Here</div><p class="lorem">Lorem ipsum dolor sit amet, consectetur adipiscing elit. Vivamus eu dui ex.</p></div></div>
  <div class="agenda-item" style="left:58px;top:117px"><span class="n">3</span><div><div class="t h-pink">Title Goes Here</div><p class="lorem">Lorem ipsum dolor sit amet, consectetur adipiscing elit. Vivamus eu dui ex.</p></div></div>
  <div class="agenda-item" style="left:228px;top:117px"><span class="n">4</span><div><div class="t h-pink">Title Goes Here</div><p class="lorem">Lorem ipsum dolor sit amet, consectetur adipiscing elit. Vivamus eu dui ex.</p></div></div>
  <div class="agenda-item" style="left:58px;top:160px"><span class="n">5</span><div><div class="t h-light">Title Goes Here</div><p class="lorem">Lorem ipsum dolor sit amet, consectetur adipiscing elit. Vivamus eu dui ex.</p></div></div>
  <div class="agenda-item" style="left:228px;top:160px"><span class="n">6</span><div><div class="t h-blue">Title Goes Here</div><p class="lorem">Lorem ipsum dolor sit amet, consectetur adipiscing elit. Vivamus eu dui ex.</p></div></div>
  <div class="foot">© 2021 Corvath Therapeutics, All Rights Reserved.<span class="num">4</span></div>
</section>

<section class="slide" style="left:232px;top:559px">
  <div class="photo" role="img" aria-label="Photo of a scientist in a lab" style="left:27px;top:0;width:203px;height:132px;background:linear-gradient(135deg,#dfe6ee,#8ea6c4 60%,#4b6b98)"></div>
  <div class="photo" role="img" aria-label="Photo of hands holding a tablet" style="left:27px;top:136px;width:100px;height:66px;background:linear-gradient(135deg,#d8e0ea,#b9a39a)"></div>
  <div class="photo" role="img" aria-label="Photo of a pharmacist among shelves" style="left:131px;top:136px;width:99px;height:66px;background:linear-gradient(135deg,#eef1f4,#c2cbd6)"></div>
  <div class="brand"><span class="mark"></span>Corvath</div>
  <h2 class="abs" style="left:250px;top:62px;font:500 16px Lexend,sans-serif;color:var(--ink)">About Us</h2>
  <p class="lorem abs" style="left:250px;top:86px;width:160px">Lorem ipsum dolor sit amet, consectetur adipiscing elit. Vivamus eu dui ex. Curabitur dapibus dignissim dui, in molestie metus feugiat sed. Praesent aliquet lorem ex, eu dapibus.</p>
  <ul class="bul lorem abs" style="left:250px;top:124px;width:160px">
    <li>Lorem ipsum dolor sit amet, consectetur adipiscing elit. Vivamus eu dui ex.</li>
    <li>Curabitur dapibus dignissim dui, in molestie metus feugiat sed.</li>
    <li>Praesent aliquet lorem ex, eu dapibus odio varius at. Duis eget tellus porta, consequat lacus vitae.</li>
    <li>Nulla facilisi. In et sollicitudin lacus. Donec risus orci, gravida sit amet risus vehicular.</li>
  </ul>
  <div class="foot">© 2021 Corvath Therapeutics, All Rights Reserved.<span class="num">5</span></div>
</section>

<section class="slide" style="left:445px;top:559px">
  <h2 class="s-title">Meet Our Team</h2>
  <div class="brand"><span class="mark"></span>Corvath</div>
  <div class="member" style="left:37px;top:64px"><div class="av" role="img" aria-label="Team member portrait"></div><div class="nm h-blue">Name Goes Here</div><div class="jt">Job Title Goes Here</div><p class="lorem">Lorem ipsum dolor sit amet, consectetur adipiscing elit. Vivamus eu dui ex. Curabitur dapibus dignissim dui.</p></div>
  <div class="member" style="left:168px;top:64px"><div class="av" role="img" aria-label="Team member portrait"></div><div class="nm h-light">Name Goes Here</div><div class="jt">Job Title Goes Here</div><p class="lorem">Lorem ipsum dolor sit amet, consectetur adipiscing elit. Vivamus eu dui ex. Curabitur dapibus dignissim dui.</p></div>
  <div class="member" style="left:299px;top:64px"><div class="av" role="img" aria-label="Team member portrait"></div><div class="nm h-pink">Name Goes Here</div><div class="jt">Job Title Goes Here</div><p class="lorem">Lorem ipsum dolor sit amet, consectetur adipiscing elit. Vivamus eu dui ex. Curabitur dapibus dignissim dui.</p></div>
  <div class="foot">© 2021 Corvath Therapeutics, All Rights Reserved.<span class="num">6</span></div>
</section>

<!-- ===== Row 3 ===== -->
<section class="slide" style="left:18px;top:684px">
  <h2 class="s-title">Slide Title Goes Here</h2>
  <div class="brand"><span class="mark"></span>Corvath</div>
  <ul class="bul lorem abs" style="left:23px;top:48px;width:190px">
    <li>Lorem ipsum dolor sit amet, consectetur adipiscing elit. Vivamus eu dui ex. Curabitur dapibus dignissim dui, in molestie metus feugiat sed.</li>
    <li>Praesent aliquet lorem ex, eu dapibus odio varius at. Duis eget tellus porta, consequat lacus vitae, venenatis dolor.</li>
    <li>Lorem ipsum dolor sit amet, consectetur adipiscing elit. Vivamus eu dui ex. Curabitur dapibus dignissim dui.</li>
  </ul>
  <div class="photo" role="img" aria-label="Photo of a scientist at a computer screen" style="left:244px;top:50px;width:157px;height:152px;background:linear-gradient(135deg,#b7c6d8,#5b7aa6 60%,#2f4f7f)"></div>
  <div class="abs" style="left:0;top:128px;width:437px;height:62px;background:var(--blue);opacity:.92"></div>
  <p class="abs" style="left:40px;top:136px;width:360px;font-size:5px;line-height:1.2;color:#fff">Lorem ipsum dolor sit amet, consectetur adipiscing elit. Vivamus eu dui ex. Curabitur dapibus dignissim dui, in molestie metus feugiat sed. Praesent aliquet lorem ex, eu dapibus odio varius at. Duis eget tellus porta, consequat lacus vitae, venenatis dolor. Nulla facilisi. In et sollicitudin lacus. Donec risus orci, gravida sit amet risus vehicula, aliquet pretium sapien. Nullam sit amet magna non ex bibendum mollis.</p>
  <div class="foot">© 2021 Corvath Therapeutics, All Rights Reserved.<span class="num">7</span></div>
</section>

<section class="slide" style="left:232px;top:684px">
  <h2 class="s-title">Slide Title Goes Here</h2>
  <div class="brand"><span class="mark"></span>Corvath</div>
  <p class="lorem abs" style="left:30px;top:46px;width:377px;text-align:center;font-size:4.6px">Lorem ipsum dolor sit amet, consectetur adipiscing elit. Vivamus eu dui ex. Curabitur dapibus dignissim dui, in molestie metus feugiat sed. Praesent aliquet lorem ex, eu dapibus odio varius at. Duis eget tellus porta, consequat lacus vitae, venenatis dolor.</p>
  <div class="feat" style="left:30px"><div class="ic" style="background:var(--blue)"><svg width="12" height="8" viewBox="0 0 12 8"><path d="M1 1 C4 7,8 1,11 7 M1 7 C4 1,8 7,11 1" stroke="#fff" stroke-width="1" fill="none"/></svg></div><div class="hd h-blue">Heading</div><p class="lorem">Lorem ipsum dolor sit amet, consectetur adipiscing elit. Vivamus eu dui ex. Curabitur dapibus dignissim dui.</p></div>
  <div class="feat" style="left:123px"><div class="ic" style="background:var(--blue-light)"><svg width="12" height="10" viewBox="0 0 12 10"><path d="M1 4 H11 A5 5 0 0 1 1 4 Z M7 4 L10 0" stroke="#fff" stroke-width="1" fill="#fff"/></svg></div><div class="hd h-light">Heading</div><p class="lorem">Lorem ipsum dolor sit amet, consectetur adipiscing elit. Vivamus eu dui ex. Curabitur dapibus dignissim dui.</p></div>
  <div class="feat" style="left:216px"><div class="ic" style="background:var(--pink)"><svg width="10" height="12" viewBox="0 0 10 12"><path d="M2 11 H8 M5 11 V6 M3 2 L7 6" stroke="#fff" stroke-width="1.2" fill="none"/></svg></div><div class="hd h-pink">Heading</div><p class="lorem">Lorem ipsum dolor sit amet, consectetur adipiscing elit. Vivamus eu dui ex. Curabitur dapibus dignissim dui.</p></div>
  <div class="feat" style="left:309px"><div class="ic" style="background:var(--orchid-2)"><svg width="10" height="12" viewBox="0 0 10 12"><path d="M3.5 1 V5 L1 11 H9 L6.5 5 V1 Z" fill="#fff"/></svg></div><div class="hd h-orchid">Heading</div><p class="lorem">Lorem ipsum dolor sit amet, consectetur adipiscing elit. Vivamus eu dui ex. Curabitur dapibus dignissim dui.</p></div>
  <div class="foot">© 2021 Corvath Therapeutics, All Rights Reserved.<span class="num">8</span></div>
</section>

<section class="slide" style="left:445px;top:684px">
  <h2 class="s-title">Slide Title Goes Here</h2>
  <div class="brand"><span class="mark"></span>Corvath</div>
  <p class="lorem abs" style="left:23px;top:48px;width:395px">Lorem ipsum dolor sit amet, consectetur adipiscing elit. Vivamus eu dui ex. Curabitur dapibus dignissim dui, in molestie metus feugiat sed. Praesent aliquet lorem ex, eu dapibus odio varius at. Duis eget tellus porta, consequat lacus vitae, venenatis dolor. Nulla facilisi. In et sollicitudin lacus.</p>
  <p class="lorem abs" style="left:23px;top:72px;width:395px">Donec risus orci, gravida sit amet risus vehicula, aliquet pretium sapien. Nullam sit amet magna non ex bibendum mollis. Nunc vel neque eu augue dignissim congue ut vitae magna. Phasellus eget commodo arcu.</p>
  <div class="photo" role="img" aria-label="Photo of lab equipment and sample racks" style="left:0;top:114px;width:410px;height:88px;background:linear-gradient(90deg,#dfe5ec,#aab8c9 50%,#6f8db4)"></div>
  <div class="abs" style="left:226px;top:114px;width:184px;height:88px;background:var(--blue-light);opacity:.85"></div>
  <p class="abs" style="left:240px;top:128px;width:160px;font-size:7px;line-height:1.15;color:#fff">Lorem ipsum dolor sit amet, consectetur adipiscing elit. Vivamus eu dui ex. Curabitur dapibus dignissim dui, in molestie metus.</p>
  <div class="foot">© 2021 Corvath Therapeutics, All Rights Reserved.<span class="num">9</span></div>
</section>

<!-- ===== Row 4 ===== -->
<section class="slide" style="left:18px;top:808px">
  <h2 class="s-title">Slide Title Goes Here</h2>
  <div class="brand"><span class="mark"></span>Corvath</div>
  <div class="col3" style="left:23px"><div class="hd h-blue">Title Goes Here!</div><ul class="bul lorem"><li>Lorem ipsum dolor sit amet, consectetur adipiscing elit. Vivamus eu dui ex. Curabitur dapibus dignissim dui.</li><li>Praesent aliquet lorem ex, eu dapibus odio varius at. Duis eget tellus porta.</li><li>Nulla facilisi. In et sollicitudin lacus. Donec risus orci, gravida sit amet.</li><li>Nullam sit amet magna non ex bibendum mollis.</li></ul></div>
  <div class="abs" style="left:150px;top:44px;width:.5px;height:130px;background:#ddd"></div>
  <div class="col3" style="left:160px"><div class="hd h-light">Title Goes Here!</div><ul class="bul lorem"><li>Lorem ipsum dolor sit amet, consectetur adipiscing elit. Vivamus eu dui ex. Curabitur dapibus dignissim dui.</li><li>Praesent aliquet lorem ex, eu dapibus odio varius at. Duis eget tellus porta.</li><li>Nulla facilisi. In et sollicitudin lacus. Donec risus orci, gravida sit amet.</li><li>Nullam sit amet magna non ex bibendum mollis.</li></ul></div>
  <div class="abs" style="left:287px;top:44px;width:.5px;height:130px;background:#ddd"></div>
  <div class="col3" style="left:297px"><div class="hd h-pink">Title Goes Here!</div><ul class="bul lorem"><li>Lorem ipsum dolor sit amet, consectetur adipiscing elit. Vivamus eu dui ex. Curabitur dapibus dignissim dui.</li><li>Praesent aliquet lorem ex, eu dapibus odio varius at. Duis eget tellus porta.</li><li>Nulla facilisi. In et sollicitudin lacus. Donec risus orci, gravida sit amet.</li><li>Nullam sit amet magna non ex bibendum mollis.</li></ul></div>
  <div class="foot">© 2021 Corvath Therapeutics, All Rights Reserved.<span class="num">10</span></div>
</section>

<section class="slide" style="left:232px;top:808px">
  <h2 class="s-title">Slide Title Goes Here</h2>
  <div class="brand"><span class="mark"></span>Corvath</div>
  <div class="tl-dot" style="left:38px;background:var(--blue)">1</div>
  <div class="tl-dot" style="left:100px;background:var(--blue-light)">2</div>
  <div class="tl-dot" style="left:162px;background:var(--pink)">3</div>
  <div class="tl-dot" style="left:224px;background:var(--orchid-2)">4</div>
  <div class="tl-dot" style="left:286px;background:var(--lilac);opacity:.7">5</div>
  <div class="tl-dot" style="left:348px;background:var(--blue)">6</div>
  <div class="tl-txt" style="left:76px;top:60px"><p>✓ Lorem ipsum dolor sit amet. Vivamus eu dui ex.</p><div class="hd h-light" style="margin-top:4px">Heading<br>Goes Here!</div></div>
  <div class="tl-txt" style="left:200px;top:60px"><p>✓ Lorem ipsum dolor sit amet. Vivamus eu dui ex.</p><div class="hd h-orchid" style="margin-top:4px">Heading<br>Goes Here!</div></div>
  <div class="tl-txt" style="left:324px;top:60px"><p>✓ Lorem ipsum dolor sit amet. Vivamus eu dui ex.</p><div class="hd h-blue" style="margin-top:4px">Heading<br>Goes Here!</div></div>
  <div class="tl-txt" style="left:14px;top:142px"><div class="hd h-blue">Heading<br>Goes Here!</div><p style="margin-top:4px">✓ Lorem ipsum dolor sit amet. Vivamus eu dui ex.</p></div>
  <div class="tl-txt" style="left:138px;top:142px"><div class="hd h-pink">Heading<br>Goes Here!</div><p style="margin-top:4px">✓ Lorem ipsum dolor sit amet. Vivamus eu dui ex.</p></div>
  <div class="tl-txt" style="left:262px;top:142px"><div class="hd" style="color:var(--lilac)">Heading<br>Goes Here!</div><p style="margin-top:4px">✓ Lorem ipsum dolor sit amet. Vivamus eu dui ex.</p></div>
  <div class="foot">© 2021 Corvath Therapeutics, All Rights Reserved.<span class="num">11</span></div>
</section>

<section class="slide" style="left:445px;top:808px">
  <h2 class="s-title">Column Chart Slide</h2>
  <div class="brand"><span class="mark"></span>Corvath</div>
  <svg class="abs" style="left:18px;top:64px" width="230" height="120" viewBox="0 0 230 120" font-family="Montserrat,sans-serif" font-size="3">
    <g fill="#444" text-anchor="end">
      <text x="6" y="12">6</text><text x="6" y="28">5</text><text x="6" y="44">4</text><text x="6" y="60">3</text><text x="6" y="76">2</text><text x="6" y="92">1</text><text x="6" y="108">0</text>
    </g>
    <g stroke="#eee" stroke-width=".4"><line x1="10" y1="11" x2="225" y2="11"/><line x1="10" y1="43" x2="225" y2="43"/><line x1="10" y1="75" x2="225" y2="75"/><line x1="10" y1="107" x2="225" y2="107"/></g>
    <rect x="25" y="42" width="6" height="65" fill="#0054AA"/><rect x="34" y="70" width="6" height="37" fill="#7BADD7"/><rect x="43" y="75" width="6" height="32" fill="#E54698"/>
    <rect x="73" y="68" width="6" height="39" fill="#0054AA"/><rect x="82" y="37" width="6" height="70" fill="#7BADD7"/><rect x="91" y="75" width="6" height="32" fill="#E54698"/>
    <rect x="121" y="56" width="6" height="51" fill="#0054AA"/><rect x="130" y="78" width="6" height="29" fill="#7BADD7"/><rect x="139" y="60" width="6" height="47" fill="#E54698"/>
    <rect x="169" y="37" width="6" height="70" fill="#0054AA"/><rect x="178" y="61" width="6" height="46" fill="#7BADD7"/><rect x="187" y="27" width="6" height="80" fill="#E54698"/>
    <g fill="#444" text-anchor="middle"><text x="37" y="113">Category 1</text><text x="85" y="113">Category 2</text><text x="133" y="113">Category 3</text><text x="181" y="113">Category 4</text></g>
    <rect x="78" y="116" width="2" height="2" fill="#0054AA"/><text x="81" y="118">Series 1</text>
    <rect x="94" y="116" width="2" height="2" fill="#7BADD7"/><text x="97" y="118">Series 2</text>
    <rect x="110" y="116" width="2" height="2" fill="#E54698"/><text x="113" y="118">Series 3</text>
  </svg>
  <div class="abs" style="left:268px;top:78px;width:145px">
    <div style="display:flex;gap:5px;margin-bottom:12px"><span style="width:6px;height:6px;background:var(--blue);flex:none"></span><div><div class="h-blue" style="font-size:5px">Title Goes Here!</div><p class="lorem">Lorem ipsum dolor sit amet, consectetur adipiscing elit. Vivamus eu dui ex.</p></div></div>
    <div style="display:flex;gap:5px;margin-bottom:12px"><span style="width:6px;height:6px;background:var(--blue-light);flex:none"></span><div><div class="h-light" style="font-size:5px">Title Goes Here!</div><p class="lorem">Lorem ipsum dolor sit amet, consectetur adipiscing elit. Vivamus eu dui ex.</p></div></div>
    <div style="display:flex;gap:5px"><span style="width:6px;height:6px;background:var(--pink);flex:none"></span><div><div class="h-pink" style="font-size:5px">Title Goes Here!</div><p class="lorem">Lorem ipsum dolor sit amet, consectetur adipiscing elit. Vivamus eu dui ex.</p></div></div>
  </div>
  <div class="foot">© 2021 Corvath Therapeutics, All Rights Reserved.<span class="num">12</span></div>
</section>

<!-- ===== Row 5 ===== -->
<section class="slide" style="left:18px;top:932px">
  <h2 class="s-title">Pie Chart Slide</h2>
  <div class="brand"><span class="mark"></span>Corvath</div>
  <svg class="abs" style="left:0;top:0" width="437" height="245" viewBox="0 0 437 245" font-family="Montserrat,sans-serif">
    <rect x="0" y="74" width="172" height="54" fill="#f6f6f6"/><rect x="0" y="134" width="172" height="54" fill="#f6f6f6"/>
    <rect x="265" y="74" width="172" height="54" fill="#f6f6f6"/><rect x="265" y="134" width="172" height="54" fill="#f6f6f6"/>
    <rect x="0" y="74" width="18" height="54" fill="#B969AE"/><rect x="0" y="134" width="18" height="54" fill="#E54698"/>
    <rect x="419" y="74" width="18" height="54" fill="#0054AA"/><rect x="419" y="134" width="18" height="54" fill="#7BADD7"/>
    <g fill="#fff" font-size="7" text-anchor="middle">
      <text transform="translate(12,101) rotate(-90)">20%</text><text transform="translate(12,161) rotate(-90)">40%</text>
      <text transform="translate(431,101) rotate(-90)">80%</text><text transform="translate(431,161) rotate(-90)">60%</text>
    </g>
    <circle cx="219" cy="132" r="69" fill="#fff"/>
    <path d="M219,132 L219,66 A66,66 0 0 1 252,189.2 Z" fill="#0054AA"/>
    <path d="M219,132 L252,189.2 A66,66 0 0 1 159.2,159.9 Z" fill="#7BADD7"/>
    <path d="M219,132 L159.2,159.9 A66,66 0 0 1 172.3,85.3 Z" fill="#E54698"/>
    <path d="M219,132 L172.3,85.3 A66,66 0 0 1 219,66 Z" fill="#B969AE"/>
    <g fill="#fff" font-size="5.5" text-anchor="middle"><text x="255" y="126">80%</text><text x="205" y="176">60%</text><text x="178" y="128">40%</text><text x="199" y="83">20%</text></g>
  </svg>
  <div class="abs" style="left:28px;top:82px;width:120px;text-align:center"><div class="h-orchid" style="font-size:5.5px">Heading</div><p class="lorem">Lorem ipsum dolor sit amet, consectetur adipiscing elit. Vivamus eu dui ex.</p></div>
  <div class="abs" style="left:28px;top:142px;width:120px;text-align:center"><div class="h-pink" style="font-size:5.5px">Heading</div><p class="lorem">Lorem ipsum dolor sit amet, consectetur adipiscing elit. Vivamus eu dui ex.</p></div>
  <div class="abs" style="left:290px;top:82px;width:120px;text-align:center"><div class="h-blue" style="font-size:5.5px">Heading</div><p class="lorem">Lorem ipsum dolor sit amet, consectetur adipiscing elit. Vivamus eu dui ex.</p></div>
  <div class="abs" style="left:290px;top:142px;width:120px;text-align:center"><div class="h-light" style="font-size:5.5px">Heading</div><p class="lorem">Lorem ipsum dolor sit amet, consectetur adipiscing elit. Vivamus eu dui ex.</p></div>
  <div class="foot">© 2021 Corvath Therapeutics, All Rights Reserved.<span class="num">13</span></div>
</section>

<section class="slide" style="left:232px;top:932px">
  <h2 class="s-title">Table Slide</h2>
  <div class="brand"><span class="mark"></span>Corvath</div>
  <div class="abs" style="left:23px;top:46px;width:93px;height:46px;background:#1f1f1f;color:#fff;font:500 9px/1.1 Lexend,sans-serif;padding:9px 5px">Title Goes<br>Here!</div>
  <div class="abs" style="left:116px;top:46px;width:87px;height:46px;background:var(--blue);color:#fff;text-align:center"><div style="font-size:4px;padding:3px 0;border-bottom:.5px solid rgba(255,255,255,.5)">Heading 1</div><div style="font:500 10px Lexend,sans-serif;padding:3px 0">2019</div><div style="font-size:3.3px;border-top:.5px solid rgba(255,255,255,.5);padding-top:3px">Text Goes Here</div></div>
  <div class="abs" style="left:204px;top:46px;width:87px;height:46px;background:var(--blue-light);color:#fff;text-align:center"><div style="font-size:4px;padding:3px 0;border-bottom:.5px solid rgba(255,255,255,.5)">Heading 2</div><div style="font:500 10px Lexend,sans-serif;padding:3px 0">2020</div><div style="font-size:3.3px;border-top:.5px solid rgba(255,255,255,.5);padding-top:3px">Text Goes Here</div></div>
  <div class="abs" style="left:292px;top:46px;width:88px;height:46px;background:var(--pink);color:#fff;text-align:center"><div style="font-size:4px;padding:3px 0;border-bottom:.5px solid rgba(255,255,255,.5)">Heading 3</div><div style="font:500 10px Lexend,sans-serif;padding:3px 0">2021</div><div style="font-size:3.3px;border-top:.5px solid rgba(255,255,255,.5);padding-top:3px">Text Goes Here</div></div>
  <table class="tbl" style="top:94px;width:357px">
    <tr><td style="width:93px">Text Goes Here</td><td class="tick" style="color:var(--blue)">✓</td><td class="tick" style="color:var(--blue-light)">✓</td><td class="tick" style="color:var(--pink)">✓</td></tr>
    <tr><td>Text Goes Here</td><td class="tick" style="color:var(--blue)">✓</td><td class="tick" style="color:var(--blue-light)">✓</td><td class="tick" style="color:var(--pink)">✓</td></tr>
    <tr><td>Text Goes Here</td><td class="tick" style="color:var(--blue)">✓</td><td class="tick" style="color:var(--blue-light)">✓</td><td class="tick" style="color:var(--pink)">✓</td></tr>
    <tr><td>Text Goes Here</td><td></td><td class="tick" style="color:var(--blue-light)">✓</td><td class="tick" style="color:var(--pink)">✓</td></tr>
    <tr><td>Text Goes Here</td><td></td><td></td><td class="tick" style="color:var(--pink)">✓</td></tr>
  </table>
  <div class="abs" style="left:23px;top:153px;width:93px;height:7px;background:#1f1f1f"></div>
  <div class="abs" style="left:116px;top:153px;width:87px;height:7px;background:var(--blue);color:#fff;font-size:3.3px;text-align:center;padding-top:1.8px">Text Goes Here</div>
  <div class="abs" style="left:204px;top:153px;width:87px;height:7px;background:var(--blue-light);color:#fff;font-size:3.3px;text-align:center;padding-top:1.8px">Text Goes Here</div>
  <div class="abs" style="left:292px;top:153px;width:88px;height:7px;background:var(--pink);color:#fff;font-size:3.3px;text-align:center;padding-top:1.8px">Text Goes Here</div>
  <div class="foot">© 2021 Corvath Therapeutics, All Rights Reserved.<span class="num">14</span></div>
</section>

<section class="slide" style="left:445px;top:932px">
  <h2 class="s-title">Slide Title Goes Here</h2>
  <div class="brand"><span class="mark"></span>Corvath</div>
  <div class="photo" role="img" aria-label="Photo of hands using a tablet at a desk" style="left:0;top:46px;width:140px;height:172px;background:linear-gradient(135deg,#e3e9ef,#a9b9cb 55%,#b89b8e)"></div>
  <div class="quote" style="left:148px;background:var(--blue)"><div class="q">“</div>Lorem ipsum dolor sit amet, consectetur adipiscing elit. Vivamus eu dui ex. Curabitur dapibus dignissim dui, in molestie metus feugiat sed. Praesent aliquet lorem ex, eu dapibus odio varius at.</div>
  <div class="quote" style="left:273px;background:var(--blue-light)"><div class="q">“</div>Lorem ipsum dolor sit amet, consectetur adipiscing elit. Vivamus eu dui ex. Curabitur dapibus dignissim dui, in molestie metus feugiat sed. Praesent aliquet lorem ex, eu dapibus dignissim dui.</div>
  <div class="foot">© 2021 Corvath Therapeutics, All Rights Reserved.<span class="num">15</span></div>
</section>

<!-- ===== Row 6: contact ===== -->
<section class="slide contact" style="left:232px;top:1057px">
  <div class="photo" role="img" aria-label="Photo of city office towers with blue and pink overlay" style="left:0;top:0;width:437px;height:245px;background:linear-gradient(135deg,#101f3c,#22426f 55%,#3a5f8f)"></div>
  <svg class="abs" style="left:0;top:0" width="437" height="245" viewBox="0 0 437 245">
    <polygon points="230,0 300,0 437,110 437,160" fill="#0054AA" opacity=".35"/>
    <polygon points="250,245 340,140 380,150 300,245" fill="#A7469A" opacity=".3"/>
  </svg>
  <div class="logo"><span class="mark"></span>Corvath Therapeutics</div>
  <div class="abs" style="left:20px;top:116px;font:500 7px Lexend,sans-serif;color:#fff">Contact Us</div>
  <div class="line" style="top:128px">Insert Company Address Here!</div>
  <div class="line" style="top:142px"><svg width="5" height="5" viewBox="0 0 10 10"><path d="M2 1 L4 1 L5 3 L4 4 C5 6 6 6 6 6 L7 5 L9 6 L9 8 C5 9 1 5 2 1 Z" fill="#fff"/></svg>Insert Phone Number</div>
  <div class="line" style="top:150px"><svg width="5" height="5" viewBox="0 0 10 10"><circle cx="5" cy="5" r="4" stroke="#fff" fill="none"/><circle cx="5" cy="5" r="1.6" stroke="#fff" fill="none"/></svg>Insert E-Mail Address</div>
  <div class="line" style="top:158px"><svg width="5" height="5" viewBox="0 0 10 10"><circle cx="5" cy="5" r="4" stroke="#fff" fill="none"/><path d="M1 5 H9 M5 1 C2 4 2 6 5 9 C8 6 8 4 5 1" stroke="#fff" fill="none" stroke-width=".7"/></svg>Insert URL Address</div>
  <div class="abs" style="left:0;width:437px;top:226px;text-align:center;font-size:3px;color:#fff">© 2021 Corvath Therapeutics, All Rights Reserved.</div>
</section>

</body>
</html>
```